Menu Edit

Hello. We need a pricing edit on our current menu and new logo swapped (we already have the new logo), as well as colour changes. Also, we require a takeaway menu, in-store menu and footpath a-frame edit as well. I have attached the files bellow.

```html
<!DOCTYPE html>
<html lang="en">
<head>
<meta charset="utf-8">
<title>Tide &amp; Ember Fish Grill – Menu</title>
<link href="https://fonts.googleapis.com/css2?family=Montserrat:ital,wght@0,400;0,500;0,600;0,700;1,500&family=Roboto+Slab:wght@700&display=swap" rel="stylesheet">
<style>
:root{
  --bg:#3a3a3a;
  --sheet:#1f1f1f;
  --red:#e0371b;
  --white:#ffffff;
  --soft:#e9e9e9;
  --line:#555555;
  --scale:.621;
}
*{box-sizing:border-box;margin:0;padding:0}
html,body{width:1200px;height:1200px;overflow:hidden;background:var(--bg)}
body{font-family:"Montserrat",Arial,sans-serif;color:var(--white)}
.stage{position:relative;width:1200px;height:1200px;background:var(--bg)}
.sheet{position:absolute;background:var(--sheet);transform-origin:0 0;transform:scale(var(--scale));overflow:hidden}
.sheet--front{left:29px;top:210px;width:898px;height:1254px}
.sheet--back{left:616px;top:209px;width:901px;height:1259px}
.block{position:absolute}
.heading{font-family:"Roboto Slab","Rockwell",Georgia,serif;font-weight:700;color:var(--red);font-size:29px;line-height:1.1;margin-bottom:8px}
.lede{font-size:12px;line-height:1.35;color:var(--soft);margin-bottom:10px}
.item{display:flex;justify-content:space-between;align-items:baseline;font-size:12.5px;font-weight:700;line-height:24px;white-space:nowrap}
.item small{font-size:10px;font-weight:500}
.item .price{font-weight:500;letter-spacing:1px;padding-left:8px}
.item .gf{font-size:9px;font-weight:500;margin-left:6px}
.desc{font-size:11.5px;line-height:1.28;color:var(--soft);font-weight:400}
.dish{margin-bottom:7px}
.dish__name{font-size:12.5px;font-weight:700;line-height:17px;display:flex;justify-content:space-between}
.dish__name small{font-size:10px;font-weight:500}
.dish__name .price{font-weight:500;letter-spacing:1px}
.boxed{border:1px solid var(--red)}
.rule{position:absolute;height:1px;background:var(--line)}

/* front */
.brand{position:absolute;left:0;top:262px;width:898px;font-size:44px;font-weight:700;letter-spacing:1px;display:flex;justify-content:center;align-items:center;gap:16px}
.brand__dot{width:16px;height:16px;border-radius:50%;background:var(--red)}
.fish{left:66px;top:469px;width:373px;height:392px;padding:5px}
.fish__inner{border:1px solid var(--red);height:100%;padding:8px 14px}
.fish .item{line-height:23px}
.prep{border-top:3px solid var(--red);margin-top:10px;padding-top:8px;text-align:center;font-size:12px;line-height:18px}
.prep b{font-weight:700}
.salads{left:462px;top:469px;width:368px;height:374px;padding:8px 15px}
.salads .lede{margin-bottom:6px}
.salads .sizes{text-align:right;font-size:12px;font-weight:700;line-height:14px;margin-bottom:2px}
.salads .sizes span{display:inline-block;width:38px;text-align:center}
.salads .dish{margin-bottom:6px}
.salads .desc{font-size:11px;line-height:1.25}
.promise{left:66px;top:876px;width:373px;height:103px;background:var(--red);padding:8px}
.promise__inner{border:1px solid var(--white);height:100%;padding:9px 18px;font-style:italic;font-weight:500;font-size:12.5px;line-height:16px}
.chips{left:461px;top:872px;width:369px}
.chips .item{line-height:18px}
.platters{left:68px;top:1003px;width:762px}
.platters .lede{margin-bottom:10px}
.platters .item{line-height:20.5px}
.platters__note{border-top:1px solid var(--line);margin-top:12px;padding-top:8px;text-align:center;font-size:12.5px}

/* back */
.starters{left:66px;top:84px;width:371px}
.starters .item{line-height:20.8px}
.kids{left:66px;top:322px;width:371px}
.kids .item{line-height:19.5px}
.different{left:462px;top:74px;width:370px;height:311px;padding:10px 16px}
.different .desc{font-size:11.5px;line-height:16px}
.sauces{left:462px;top:396px;width:370px}
.bev{left:66px;top:496px;width:766px;display:flex;justify-content:space-between}
.bev__col{width:360px}
.bev__col .item{line-height:21.6px}
.bev__sub{font-size:12.5px;font-weight:600;line-height:18px;margin:-2px 0 6px}
.bev__right{width:386px;padding-top:40px}
.bev__right .item{line-height:23.2px;font-size:12px}
.bev__right .item small{font-size:10px}
.desserts{left:66px;top:731px;width:766px;height:201px;padding:8px 18px}
.desserts__grid{display:grid;grid-template-columns:1fr 1fr;column-gap:60px}
.desserts .dish__name{line-height:20px}
.desserts .desc{font-size:12px;line-height:18px}
.desserts .row{display:flex;justify-content:space-between}
.desserts hr{grid-column:1/3;border:0;border-top:1px solid #666;margin:8px 0 10px}
.notes{left:66px;top:950px;width:766px;text-align:center;font-size:12.5px;font-weight:700;line-height:19.5px}
.eco{display:inline-block;width:13px;height:13px;border:1.5px solid var(--white);border-radius:50%;vertical-align:-2px}
.offer{left:70px;top:1020px;width:762px;border-top:1px solid #666;border-bottom:1px solid #666;padding:4px 0 7px;text-align:center;font-size:14.5px;font-weight:500;line-height:24px;letter-spacing:.5px}
.hours{left:56px;top:1084px;width:380px;text-align:right}
.hours__title{font-family:"Roboto Slab","Rockwell",Georgia,serif;font-weight:700;color:var(--red);font-size:27px;line-height:32px;margin-bottom:4px}
.hours p{font-size:13.5px;line-height:23.5px;white-space:nowrap}
.hours b{font-weight:700}
.phone{left:452px;top:1088px;width:372px;height:63px;background:var(--white);color:#111;display:flex;align-items:center;justify-content:center;gap:14px;font-size:46px;font-weight:700;letter-spacing:1px}
.mail{left:452px;top:1161px;width:372px;height:32px;background:var(--red);display:flex;align-items:center;justify-content:center;gap:8px;font-size:16px;font-weight:600}
</style>
</head>
<body>
<main class="stage">

  <section class="sheet sheet--front" aria-label="Menu front">
    <div class="brand"><span class="brand__dot"></span>TIDE &amp; EMBER FISH GRILL</div>

    <div class="block fish">
      <div class="fish__inner">
        <h2 class="heading">Fish &amp; Chips</h2>
        <p class="lede">Served with your choice of chips, homemade tartare sauce, lemon &amp; parsley.</p>
        <div class="item"><span>Classic Cod <small>with chips</small></span><span class="price">12.9</span></div>
        <div class="item"><span>Crumbed Whiting <small>(QLD) with chips</small></span><span class="price">15.9</span></div>
        <div class="item"><span>Snapper <small>(QLD, LC) with chips</small></span><span class="price">18.9</span></div>
        <div class="item"><span>Ocean Barramundi <small>(QLD, FRM) with chips</small></span><span class="price">18.9</span></div>
        <div class="item"><span>Crispy Skin Salmon <small>(TAS, FRM) with chips</small></span><span class="price">18.9</span></div>
        <div class="item"><span>Crispy Skin Ocean Trout <small>(TAS, FRM) with chips</small></span><span class="price">18.9</span></div>
        <div class="item"><span>Crumbed Calamari (8) <small>with chips</small></span><span class="price">12.9</span></div>
        <div class="item"><span>Salt &amp; Pepper Calamari (8) <small>with chips</small></span><span class="price">13.9</span></div>
        <div class="item"><span>BBQ Prawn Skewers (2) <small>with chips</small></span><span class="price">22.9</span></div>
        <div class="prep"><b>Choose your preparation:</b><br>PANKO CRUMBED / TEMPURA BATTERED / GRILLED</div>
      </div>
    </div>

    <div class="block salads boxed">
      <h2 class="heading">Salads</h2>
      <p class="lede">Freshly prepared to order using the freshest local produce.</p>
      <div class="sizes">Full / Side<br><span>10</span><span>7</span></div>
      <div class="dish"><div class="dish__name">Greek</div><p class="desc">Lettuce, cucumber, tomato, red onion, Greek olives, feta, wild oregano, tossed in Greek extra virgin olive oil vinaigrette.</p></div>
      <div class="dish"><div class="dish__name">Coleslaw</div><p class="desc">Red &amp; green cabbage, eschallots, carrot, tossed in a light mayonnaise dressing.</p></div>
      <div class="dish"><div class="dish__name">Crunchy Asian Slaw</div><p class="desc">Red &amp; green cabbage, eschallots, carrot, coriander, crispy noodles, tossed in a light soy dressing.</p></div>
      <div class="dish"><div class="dish__name">Roast Pumpkin &amp; Wild Rocket</div><p class="desc">Roast pumpkin, wild rocket, freshly shaved Parmigiano Reggiano, toasted pine nuts, tossed in Greek extra virgin olive oil &amp; vintage balsamic vinegar.</p></div>
    </div>

    <div class="block promise">
      <p class="promise__inner">Our premium quality fish is line caught (LC) and farmed (FRM) from pristine Australian waters, delivered in-store every morning for you to enjoy market fresh!</p>
    </div>

    <div class="block chips">
      <h2 class="heading">Chips</h2>
      <div class="item"><span>Beer Battered Chips</span><span class="price">5</span></div>
      <div class="item"><span>Classic Chips<span class="gf">GF</span></span><span class="price">5</span></div>
      <div class="item"><span>Sweet Potato Chips<span class="gf">GF</span></span><span class="price">5</span></div>
      <div class="item"><span>Greek style chips with feta &amp; wild oregano</span><span class="price">7</span></div>
    </div>

    <div class="block platters">
      <h2 class="heading">Cooked Seafood Platters</h2>
      <p class="lede">Cooked Seafood Platters include: Queensland whiting, calamari, salt &amp; pepper calamari, ocean king prawns, sea scallops, beer battered chips, one of our freshly made salads, homemade tartare sauce, lemon &amp; parsley.</p>
      <div class="item"><span>Cooked Platter for One</span><span class="price">21.9</span></div>
      <div class="item"><span>Cooked Platter for Two</span><span class="price">41.9</span></div>
      <div class="item"><span>Cooked Platter for Three</span><span class="price">61.9</span></div>
      <p class="platters__note">Our seafood platters are available panko crumbed only.</p>
    </div>
  </section>

  <section class="sheet sheet--back" aria-label="Menu back">
    <div class="block starters">
      <h2 class="heading">Starters &amp; Sides</h2>
      <div class="item"><span>Crumbed Calamari (8)</span><span class="price">8</span></div>
      <div class="item"><span>Salt &amp; Pepper Calamari (8)</span><span class="price">9</span></div>
      <div class="item"><span>Potato Scallop</span><span class="price">2</span></div>
      <div class="item"><span>Crumbed Ocean King Prawn Cutlets (2)</span><span class="price">9</span></div>
      <div class="item"><span>Crumbed Sea Scallops (2)</span><span class="price">7</span></div>
      <div class="item"><span>BBQ Prawn Skewer</span><span class="price">9</span></div>
      <div class="item"><span>Grilled Halloumi (3)</span><span class="price">10</span></div>
    </div>
    <div class="rule" style="left:66px;top:297px;width:371px"></div>

    <div class="block kids">
      <h2 class="heading">Kid’s Fish &amp; Chips</h2>
      <p class="lede">Served with sauce.</p>
      <div class="item"><span>Crumbed Cod Bites <small>with chips</small></span><span class="price">9</span></div>
      <div class="item"><span>Crumbed Calamari (4) <small>with chips</small></span><span class="price">9</span></div>
      <div class="item"><span>Real Chicken Nuggets <small>with chips</small></span><span class="price">9</span></div>
    </div>

    <div class="block different boxed">
      <h2 class="heading">Something Different</h2>
      <div class="dish"><div class="dish__name"><span>Fish Burger <small>with chips</small></span><span class="price">13.9</span></div><p class="desc">Crumbed cod fillet, lettuce, tomato &amp; homemade tartare sauce in a sesame bun.</p></div>
      <div class="dish"><div class="dish__name"><span>Fish Tacos (3) <small>with chips</small></span><span class="price">13.9</span></div><p class="desc">Tempura battered cod, shredded cabbage, smokey chipotle mayonnaise &amp; coriander in soft flour tortillas.</p></div>
      <div class="dish"><div class="dish__name"><span>Grilled Chicken Burger <small>with chips</small></span><span class="price">14.9</span></div><p class="desc">Grilled chicken breast, cheddar cheese, lettuce, tomato, fresh avocado &amp; aioli in a sesame bun.</p></div>
      <div class="dish"><div class="dish__name"><span>Grilled Steak Burger <small>with chips</small></span><span class="price">13.9</span></div><p class="desc">Tender “grass fed” rib fillet, caramelised onion, Swiss cheese, lettuce &amp; tomato with whiskey BBQ sauce in a sesame bun.</p></div>
    </div>

    <div class="block sauces">
      <h2 class="heading">Sauces</h2>
      <div class="item"><span>Homemade Tartare, Aioli, Tomato &amp; Sweet Chilli</span><span class="price">1</span></div>
    </div>
    <div class="rule" style="left:66px;top:480px;width:766px"></div>

    <div class="block bev">
      <div class="bev__col">
        <h2 class="heading">Beverages</h2>
        <p class="bev__sub">COFFEE BY CREMA HOUSE</p>
        <div class="item"><span>Espresso</span><span class="price">3</span></div>
        <div class="item"><span>Flat White</span><span class="price">4</span></div>
        <div class="item"><span>Cappuccino</span><span class="price">4</span></div>
        <div class="item"><span>Long Black</span><span class="price">4</span></div>
        <div class="item"><span>Macchiato</span><span class="price">4</span></div>
        <div class="item"><span>Chai Latte</span><span class="price">4</span></div>
        <div class="item"><span>Hot Mocha</span><span class="price">4</span></div>
      </div>
      <div class="bev__col bev__right">
        <div class="item"><span>Hot Chocolate</span><span class="price">4</span></div>
        <div class="item"><span>Iced Latte</span><span class="price">4</span></div>
        <div class="item"><span>Iced Chocolate</span><span class="price">7</span></div>
        <div class="item"><span>Iced Coffee</span><span class="price">7</span></div>
        <div class="item"><span>Iced Frappe <small>(Coffee, Chocolate, Mocha)</small></span><span class="price">7</span></div>
        <div class="item"><span>MILKSHAKES <small>(Chocolate, Strawberry, Vanilla Malt, Caramel)</small></span><span class="price">5</span></div>
        <div class="item"><span>THICKSHAKES <small>(Chocolate, Strawberry, Vanilla Malt, Caramel)</small></span><span class="price">7</span></div>
      </div>
    </div>

    <div class="block desserts boxed">
      <h2 class="heading">Desserts</h2>
      <div class="desserts__grid">
        <div>
          <div class="dish__name">Gelato by Nuvola</div>
          <p class="desc row"><span>Single Scoop</span><span>5</span></p>
          <p class="desc row"><span>Double Scoop</span><span>7</span></p>
        </div>
        <div>
          <div class="dish__name"><span>Greek Delights</span><span class="price">4</span></div>
          <p class="desc">Traditional recipe made by confectioners in Australia.</p>
        </div>
        <hr>
        <div>
          <div class="dish__name">Greek Baklava</div>
          <p class="desc row"><span>Layers of golden syrupy pastry filled with nuts.</span><span>4</span></p>
          <p class="desc row"><span>Enjoy as is or with a scoop of vanilla bean gelato.</span><span>8</span></p>
        </div>
        <div>
          <div class="dish__name"><span>Greek Shortbread Biscuits</span><span class="price">3</span></div>
          <p class="desc">Traditional Greek shortbread biscuits rolled in fragrant icing sugar.</p>
        </div>
      </div>
    </div>

    <p class="block notes">Our seafood is deep-fried to golden goodness with premium 100% Australian grown and pressed canola oil.<br>Gluten friendly options are available. Our takeaway packaging is <span class="eco"></span> friendly. Public Holiday surcharge 15%.<br>Menu substitutions are not available. Menu 2021.</p>

    <p class="block offer">CASUAL DINING | TAKEAWAY | ONLINE ORDERING &amp; DELIVERY | FRESH RETAIL<br>BYO Welcome! Wine, Beer &amp; Spirits / Soft Drinks Available</p>

    <div class="block hours">
      <h2 class="hours__title">Open Every Day</h2>
      <p><b>Mon – Thurs</b> 5pm to 9pm • <b>Fri – Sun</b> 12pm to 9pm</p>
      <p>Shop 3/118 Harbour Lane, Riverbend QLD 4100</p>
      <p><b>www.tideandember.com.au</b></p>
    </div>

    <div class="block phone">
      <svg width="46" height="38" viewBox="0 0 46 38" aria-hidden="true"><path d="M4 14c0-6 8-10 19-10s19 4 19 10v3h-9v-4c-3-1-6-1.5-10-1.5S16 12 13 13v4H4z" fill="#e0371b"/><path d="M12 18h22l5 16H7z" fill="#e0371b"/><g fill="#fff"><rect x="17" y="21" width="3" height="3"/><rect x="22" y="21" width="3" height="3"/><rect x="27" y="21" width="3" height="3"/><rect x="16" y="26" width="3" height="3"/><rect x="22" y="26" width="3" height="3"/><rect x="28" y="26" width="3" height="3"/></g></svg>
      <span>3555 0142</span>
    </div>
    <div class="block mail">
      <svg width="20" height="14" viewBox="0 0 20 14" aria-hidden="true"><rect x="1" y="1" width="18" height="12" fill="none" stroke="#fff" stroke-width="1.5"/><path d="M1 1l9 7 9-7" fill="none" stroke="#fff" stroke-width="1.5"/></svg>
      <span>hello@tideandember.com.au</span>
    </div>
  </section>

</main>
</body>
</html>
```